Korvanta

1. We need a four color business card
2. The Front of card needs to include our Logo, Slogan which is "Launching, Expanding & Optimizing Organizations, Individual Name, email, two phone numbers, email, skype address, website address
3. Back of card needs to include the following topics: Start Ups & Business Optimization,Product Acquisition, Destination Product Marketing & Representation,Marketing & Sales, Operations, Training/Education, Digital Marketing, Keynote Addresses/Public Speaking
3. Back of card can not be black as it needs to be a color that people can write on
Industry/Entity Type
Business

```html
<!DOCTYPE html>
<html lang="en">
<head>
<meta charset="utf-8">
<title>Korvanta – Business Card</title>
<link rel="stylesheet" href="https://fonts.googleapis.com/css2?family=PT+Sans:wght@400;700&family=Arimo:wght@400&family=Archivo+Narrow:wght@400&display=swap">
<style>
  :root {
    --board: #808083;
    --sky: #9ed7f1;
    --sky-soft: #d8f0fb;
    --paper: #ffffff;
    --meadow: #bfd593;
    --meadow-soft: #e6efd2;
    --leaf: #8cc43f;
    --brand-blue: #2a67a9;
    --ink: #555a5e;
    --ink-soft: #6a6e72;
    --label: #000000;
  }
  html, body {
    margin: 0;
    padding: 0;
    width: 1059px;
    height: 1200px;
    overflow: hidden;
    background: var(--board);
  }
  .board {
    position: relative;
    width: 1059px;
    height: 1200px;
    background: var(--board);
  }
  .card {
    position: absolute;
    left: 107px;
    width: 660px;
    height: 377px;
    border-radius: 26px;
    overflow: hidden;
    background: var(--paper);
    box-shadow: 0 0 0 2px #ffffff;
  }
  .card--front { top: 151px; }
  .card--back  { top: 569px; }
  .card__art {
    position: absolute;
    inset: 0;
    width: 660px;
    height: 377px;
  }
  .side-label {
    position: absolute;
    left: 833px;
    font-family: "Arimo", Arial, sans-serif;
    font-size: 58px;
    color: var(--label);
    margin: 0;
    line-height: 1;
  }
  .side-label--front { top: 290px; }
  .side-label--back  { top: 734px; }

  .brand {
    position: absolute;
    display: flex;
    align-items: center;
    gap: 14px;
  }
  .brand__dot {
    border-radius: 50%;
    background: var(--brand-blue);
  }
  .brand__name {
    font-family: "PT Sans", sans-serif;
    font-weight: 400;
    color: var(--brand-blue);
    line-height: 1;
  }
  .card--front .brand { left: 30px; top: 44px; }
  .card--front .brand__dot { width: 96px; height: 96px; }
  .card--front .brand__name { font-size: 54px; }

  .slogan {
    position: absolute;
    left: 84px;
    top: 145px;
    margin: 0;
    font-family: "PT Sans", sans-serif;
    font-variant: small-caps;
    font-size: 12.5px;
    letter-spacing: 0.4px;
    color: var(--ink-soft);
  }
  .contact {
    position: absolute;
    left: 438px;
    top: 210px;
  }
  .contact__name {
    margin: 0 0 10px;
    font-family: "PT Sans", sans-serif;
    font-weight: 400;
    font-size: 32px;
    color: var(--brand-blue);
    line-height: 1;
  }
  .contact__list {
    list-style: none;
    margin: 0;
    padding: 0;
    font-family: "Arimo", Arial, sans-serif;
    font-size: 15px;
    line-height: 19.5px;
    color: var(--ink);
  }
  .contact__indent { padding-left: 31px; }

  .services {
    position: absolute;
    left: 0;
    right: 0;
    top: 22px;
    margin: 0;
    padding: 0;
    list-style: none;
    text-align: center;
    font-family: "Archivo Narrow", "Arial Narrow", sans-serif;
    color: var(--ink);
    line-height: 1;
  }
  .services li { margin-bottom: 9px; }
  .services .s-sm { font-size: 16px; }
  .services .s-md { font-size: 18px; }
  .services .s-lg { font-size: 21px; }

  .card--back .brand { left: 128px; top: 244px; }
  .card--back .brand__dot { width: 104px; height: 104px; }
  .card--back .brand__name { font-size: 56px; }
</style>
</head>
<body>
<main class="board">

  <section class="card card--front" aria-label="Business card front">
    <svg class="card__art" viewBox="0 0 660 377" aria-hidden="true">
      <defs>
        <linearGradient id="front-sky" x1="0" y1="0" x2="1" y2="0">
          <stop offset="0" stop-color="var(--sky)"/>
          <stop offset="0.45" stop-color="var(--sky-soft)"/>
          <stop offset="0.75" stop-color="var(--paper)"/>
        </linearGradient>
        <linearGradient id="front-meadow" x1="0" y1="0" x2="1" y2="1">
          <stop offset="0" stop-color="var(--paper)"/>
          <stop offset="0.5" stop-color="var(--meadow-soft)"/>
          <stop offset="1" stop-color="var(--meadow)"/>
        </linearGradient>
      </defs>
      <rect width="660" height="377" fill="url(#front-sky)"/>
      <path d="M157,377 C330,330 470,200 552,107 L660,60 L660,377 Z" fill="url(#front-meadow)"/>
      <path d="M0,251 C150,300 380,240 552,107 C470,200 330,330 157,377 L0,377 Z" fill="var(--paper)"/>
      <path d="M0,251 C150,300 380,240 552,107" fill="none" stroke="var(--leaf)" stroke-width="2"/>
      <path d="M157,377 C330,330 470,200 552,107" fill="none" stroke="var(--leaf)" stroke-width="2"/>
    </svg>
    <svg class="card__art" viewBox="0 0 660 377" role="img" aria-label="Outline of an airplane climbing">
      <ellipse cx="580" cy="88" rx="40" ry="18" fill="var(--meadow-soft)" opacity="0.8"/>
    </svg>

    <div class="brand">
      <span class="brand__dot"></span>
      <span class="brand__name">Korvanta</span>
    </div>
    <p class="slogan">Launching, Expanding &amp; Optimizing Organizations</p>

    <div class="contact">
      <h1 class="contact__name">Mara Lindqvist</h1>
      <ul class="contact__list">
        <li>Tel: +00 (000)000-00-00</li>
        <li class="contact__indent">+00 (000)000-00-00</li>
        <li>email: mara@korvantamail.com</li>
        <li>skype: mara.korv</li>
        <li>korvanta.com</li>
      </ul>
    </div>
  </section>
  <p class="side-label side-label--front">Front</p>

  <section class="card card--back" aria-label="Business card back">
    <svg class="card__art" viewBox="0 0 660 377" aria-hidden="true">
      <defs>
        <linearGradient id="back-sky" x1="0" y1="0" x2="1" y2="0">
          <stop offset="0" stop-color="var(--sky)"/>
          <stop offset="0.4" stop-color="var(--sky-soft)"/>
          <stop offset="0.7" stop-color="var(--paper)"/>
        </linearGradient>
        <linearGradient id="back-meadow" x1="0" y1="0" x2="0" y2="1">
          <stop offset="0.45" stop-color="var(--paper)" stop-opacity="0"/>
          <stop offset="1" stop-color="var(--meadow)"/>
        </linearGradient>
        <linearGradient id="back-arc" x1="0" y1="1" x2="1" y2="0">
          <stop offset="0" stop-color="var(--leaf)"/>
          <stop offset="0.6" stop-color="var(--meadow)"/>
          <stop offset="1" stop-color="var(--meadow-soft)" stop-opacity="0.3"/>
        </linearGradient>
      </defs>
      <rect width="660" height="377" fill="url(#back-sky)"/>
      <rect width="660" height="377" fill="url(#back-meadow)"/>
      <path d="M240,0 C560,20 640,150 520,250 C420,330 200,365 0,372" fill="none" stroke="url(#back-arc)" stroke-width="14" opacity="0.85"/>
      <path d="M260,4 C540,28 610,140 500,236" fill="none" stroke="var(--paper)" stroke-width="10" opacity="0.7"/>
    </svg>

    <ul class="services">
      <li class="s-sm">Start Ups &amp; Business Optimization</li>
      <li class="s-sm">Product Acquisition</li>
      <li class="s-lg">Destination Product Marketing &amp; Representation</li>
      <li class="s-lg">Marketing &amp; Sales</li>
      <li class="s-lg">Operations</li>
      <li class="s-md">Training/Education</li>
      <li class="s-md">Digital Marketing</li>
      <li class="s-sm">Keynote Addresses/Public Speaking</li>
    </ul>

    <div class="brand">
      <span class="brand__dot"></span>
      <span class="brand__name">Korvanta</span>
    </div>
  </section>
  <p class="side-label side-label--back">Back</p>

</main>
</body>
</html>
```